Fernbrook Plots - Online-only garden installation company

Online-only garden installation company. Our demographic is middle aged / suburban women, and we anticipate Facebook driving traffic to this website, as well as referrals from garden centers. The website must be very simple in design and function.

All orders will be placed through the website, including size of garden (3 options), location in yard, payment, and scheduling of installation date.

The website should employ a 3 step process:

Step 1: Select garden size. Either an 4' X 4', 8' X 4', or 12' X 4'.

Step 2: Select a location. We would like to use google maps to look up a US address, then "drag and drop" one of the garden sizes from step 1 to the location the customer would like us to install the garden at their home.

Step 3: Pick an installation date and pay. Using an online calendar the customer will pick a date, and then pay for the installation via credit card.

The website will be linked to an email account, FernbrookPlots@mailzy.com to inform us of orders placed.

Target Market(s)

Our demographic is middle aged / suburban women, and we anticipate Facebook driving traffic to this website, as well as referrals from garden centers.

Industry/Entity Type

Coding

Number of Pages Required

Requirements
Must have
• Scheduling and payment options.

```html
<!DOCTYPE html>
<html lang="en">
<head>
<meta charset="utf-8">
<title>Fernbrook Plots – Garden Installation</title>
<link rel="stylesheet" href="https://fonts.googleapis.com/css2?family=Open+Sans:wght@400;600;700&family=Roboto+Slab:wght@300;400&display=swap">
<style>
:root{
  --orange:#e0622b;
  --orange-dark:#c9521f;
  --green:#3b8139;
  --green-dark:#2f6e2f;
  --ink:#333333;
  --text:#555555;
  --muted:#8a8a8a;
  --line:#e3e3e3;
  --footer:#3b3a38;
  --footer-text:#cfcfcf;
  --white:#ffffff;
}
*{box-sizing:border-box;margin:0;padding:0}
html,body{width:1200px;height:3409px;overflow:hidden}
body{position:relative;background:var(--white);font-family:"Open Sans",Arial,sans-serif;color:var(--text)}
a{color:inherit;text-decoration:none}
.abs{position:absolute}
.heading{font-family:"Roboto Slab",Georgia,serif;font-weight:300;color:var(--ink);text-transform:uppercase;letter-spacing:.5px}
.mark-dot{width:22px;height:22px;border-radius:50%;background:var(--orange);left:589px}

/* header */
.site-header{position:absolute;left:0;top:0;width:1200px;height:141px}
.top-actions{position:absolute;right:0;top:0;height:36px;display:flex}
.top-actions a{display:flex;align-items:center;gap:7px;color:var(--white);font-size:11px;text-transform:uppercase;letter-spacing:.3px;padding:0 22px;clip-path:polygon(10px 0,100% 0,100% 100%,0 100%)}
.top-actions .order{background:var(--green);width:140px;justify-content:center}
.top-actions .account{background:var(--ink);width:116px;justify-content:center}
.top-actions .cart{background:var(--orange);width:206px;justify-content:flex-start;padding-left:34px}
.brand{position:absolute;left:80px;top:40px;display:flex;align-items:center;gap:10px}
.brand .dot{width:18px;height:18px;border-radius:50%;background:var(--orange)}
.brand .name{font-family:"Roboto Slab",Georgia,serif;font-weight:400;font-size:19px;color:var(--ink);text-transform:uppercase;letter-spacing:1px}
.main-nav{position:absolute;left:386px;top:74px;display:flex;gap:0}
.main-nav a{font-size:11.5px;color:var(--ink);text-transform:uppercase;margin-right:28px;padding-bottom:5px}
.main-nav a.active{color:var(--orange);border-bottom:2px solid var(--orange)}
.search{position:absolute;left:859px;top:68px;width:268px;height:30px;border-radius:15px;background:#f1f1f1;display:flex;align-items:center;padding:0 14px;font-size:11px;color:#777;justify-content:space-between}

/* hero */
.hero{position:absolute;left:0;top:141px;width:1200px;height:552px;background:linear-gradient(160deg,#6f8a58 0%,#4f6b3d 35%,#8aa27a 60%,#3d4f32 100%)}
.hero-photo{position:absolute;inset:0}
.booking{position:absolute;left:0;bottom:0;width:1200px;height:120px;background:rgba(30,30,30,.72)}
.booking h2{position:absolute;top:17px;width:100%;text-align:center;color:var(--white);font-family:"Roboto Slab",Georgia,serif;font-weight:400;font-size:20px;text-transform:uppercase}
.field{position:absolute;top:57px;height:45px;background:var(--white);border-radius:3px;font-size:11px;color:#888;display:flex;align-items:center;padding-left:14px}
.field .icon{position:absolute;right:0;top:0;width:40px;height:45px;display:flex;align-items:center;justify-content:center;border-left:1px solid var(--line)}
.search-btn{position:absolute;left:916px;top:57px;width:125px;height:45px;background:var(--orange);color:var(--white);border-radius:3px;font-size:12px;font-weight:700;display:flex;align-items:center;justify-content:center;gap:8px;text-transform:uppercase}

/* welcome */
.welcome .title{top:808px;width:100%;text-align:center;font-size:22px}
.welcome p{top:857px;left:257px;width:686px;text-align:center;font-size:13px;line-height:24px;color:var(--muted)}
.more-link{font-size:11.5px;font-weight:700;color:var(--orange);text-transform:uppercase;display:flex;align-items:center;gap:4px}

/* services */
.services-band{left:0;top:1168px;width:432px;height:78px;background:var(--orange);color:var(--white);font-family:"Roboto Slab",Georgia,serif;font-weight:300;font-size:23px;text-transform:uppercase;display:flex;align-items:center;padding-left:73px}
.services-tab{left:1127px;top:1168px;width:73px;height:78px;background:var(--orange)}
.services-photo{left:443px;top:1102px;width:675px;height:432px;background:linear-gradient(135deg,#5a4330 0%,#7c9a3c 35%,#e9c94a 55%,#4d3a2a 100%);box-shadow:0 0 0 6px var(--white),0 2px 12px rgba(0,0,0,.18)}
.services p{left:73px;top:1283px;width:336px;font-size:13px;line-height:24px;color:var(--muted)}

/* projects */
.projects .title{top:1678px;width:100%;text-align:center;font-size:22px}
.tile{box-shadow:0 2px 8px rgba(0,0,0,.18)}

/* testimonial */
.testimonial{left:0;top:2462px;width:1200px;height:418px;background:var(--green);color:var(--white);text-align:center}
.quote-mark{position:absolute;left:569px;top:56px;width:62px;height:62px;border:3px solid var(--white);border-radius:50%;display:flex;align-items:center;justify-content:center;font-family:"Roboto Slab",Georgia,serif;font-size:44px;line-height:1;padding-top:14px}
.testimonial blockquote{position:absolute;top:144px;left:250px;width:700px;font-size:16px;line-height:28px}
.testimonial .rule{position:absolute;left:582px;top:238px;width:36px;height:1px;background:rgba(255,255,255,.7)}
.testimonial .who{position:absolute;top:250px;width:100%;font-family:"Roboto Slab",Georgia,serif;font-size:16px}
.testimonial .role{position:absolute;top:282px;width:100%;font-size:12px}
.slider-nav{position:absolute;left:570px;top:336px;display:flex;gap:4px}
.slider-nav span{width:28px;height:28px;border:2px solid var(--white);border-radius:50%;display:flex;align-items:center;justify-content:center}

/* call to action */
.cta{left:0;top:2880px;width:1200px;height:239px;background:linear-gradient(90deg,#4b3526 0%,#6d5641 30%,#3c2f26 55%,#8b8170 80%,#4a3a2d 100%)}
.cta-shade{position:absolute;inset:0;background:rgba(0,0,0,.35)}
.cta h2{position:absolute;top:74px;width:100%;text-align:center;color:var(--white);font-family:"Roboto Slab",Georgia,serif;font-weight:400;font-size:22px;text-transform:uppercase}
.cta .btn{position:absolute;left:499px;top:116px;width:203px;height:46px;background:var(--orange);color:var(--white);font-size:12.5px;font-weight:700;text-transform:uppercase;display:flex;align-items:center;justify-content:center;border-radius:2px}

/* footer */
.site-footer{left:0;top:3119px;width:1200px;height:290px;background:var(--footer);color:var(--footer-text)}
.footer-brand{position:absolute;left:92px;top:116px;font-family:"Roboto Slab",Georgia,serif;font-size:17px;color:var(--white);text-transform:uppercase;letter-spacing:1px;display:flex;align-items:center;gap:8px}
.footer-brand .dot{width:14px;height:14px;border-radius:50%;background:var(--white)}
.footer-col{position:absolute;top:40px}
.footer-col h4{font-family:"Roboto Slab",Georgia,serif;font-weight:400;font-size:14px;color:var(--white);margin-bottom:12px}
.footer-col li{list-style:none;font-size:11.5px;line-height:22px}
.cards{display:grid;grid-template-columns:repeat(3,44px);gap:8px}
.cards span{height:30px;border-radius:3px;background:#e9e9e9}
.socials{display:flex;gap:6px}
.socials span{width:34px;height:34px;background:#777}
.copyright{position:absolute;left:73px;top:247px;font-size:11px;color:var(--footer-text)}
</style>
</head>
<body>

<header class="site-header">
  <nav class="top-actions">
    <a class="order" href="#">
      <svg width="12" height="12" viewBox="0 0 12 12"><path d="M1 6 L11 1 L7 11 L6 7 Z" fill="none" stroke="#fff" stroke-width="1.2"/></svg>Order Now</a>
    <a class="account" href="#">
      <svg width="12" height="12" viewBox="0 0 12 12"><circle cx="6" cy="4" r="2.5" fill="none" stroke="#fff"/><path d="M1.5 11.5 Q6 5.5 10.5 11.5" fill="none" stroke="#fff"/></svg>My Account</a>
    <a class="cart" href="#">
      <svg width="13" height="12" viewBox="0 0 13 12"><path d="M0.5 1 H3 L4.5 8 H11 L12 3 H3.5" fill="none" stroke="#fff"/><circle cx="5" cy="10.5" r="1" fill="#fff"/><circle cx="10" cy="10.5" r="1" fill="#fff"/></svg>(0) Items</a>
  </nav>
  <a class="brand" href="#"><span class="dot"></span><span class="name">Fernbrook Plots</span></a>
  <nav class="main-nav">
    <a class="active" href="#">Home</a><a href="#">About Us</a><a href="#">Services</a><a href="#">Projects</a><a href="#">Shop</a><a href="#">Contact Us</a>
  </nav>
  <div class="search"><span>Enter Your Keywords...</span>
    <svg width="12" height="12" viewBox="0 0 12 12"><circle cx="5" cy="5" r="3.8" fill="none" stroke="#555" stroke-width="1.4"/><path d="M8 8 L11 11" stroke="#555" stroke-width="1.6"/></svg></div>
</header>

<section class="hero">
  <div class="hero-photo" role="img" aria-label="Gloved hands holding a potted seedling in a green garden"></div>
  <form class="booking">
    <h2>Order Now Garden Installation Today</h2>
    <div class="field" style="left:159px;width:243px">Select garden size
      <span class="icon"><svg width="10" height="6" viewBox="0 0 10 6"><path d="M0 0 H10 L5 6 Z" fill="#777"/></svg></span></div>
    <div class="field" style="left:411px;width:244px">Select a location
      <span class="icon"><svg width="16" height="16" viewBox="0 0 16 16"><circle cx="8" cy="8" r="5" fill="none" stroke="#777" stroke-width="1.4"/><circle cx="8" cy="8" r="1.8" fill="#777"/><path d="M8 0V3M8 13V16M0 8H3M13 8H16" stroke="#777" stroke-width="1.4"/></svg></span></div>
    <div class="field" style="left:664px;width:241px">Pick an installation date
      <span class="icon"><svg width="15" height="14" viewBox="0 0 15 14"><rect x="1" y="2" width="13" height="11" fill="none" stroke="#777" stroke-width="1.3"/><path d="M1 5H14M4 0V3M11 0V3" stroke="#777" stroke-width="1.3"/></svg></span></div>
    <a class="search-btn" href="#">
      <svg width="14" height="14" viewBox="0 0 12 12"><circle cx="5" cy="5" r="3.8" fill="none" stroke="#fff" stroke-width="1.4"/><path d="M8 8 L11 11" stroke="#fff" stroke-width="1.6"/></svg>Search</a>
  </form>
</section>

<section class="welcome">
  <span class="abs mark-dot" style="top:760px"></span>
  <h2 class="abs heading title">Welcome to Fernbrook Plots</h2>
  <p class="abs">Lorem ipsum dolor sit amet, consectetur adipisicing elit, sed do eiusmod tempor incididunt ut labore et dolore magna aliqua. Ut enim ad minim veniam, quis nostrud exercitation ullamco laboris nisi ut aliquip ex ea commodo consequat. Duis aute irure dolor in reprehenderit in voluptate velit esse cillum dolore eu fugiat nulla pariatur. Excepteur sint occaecat cupidatat non proident, sunt in culpa qui officia deserunt mollit anim id est laborum.</p>
  <a class="abs more-link" style="left:551px;top:1003px" href="#">Learn More
    <svg width="10" height="10" viewBox="0 0 10 10"><circle cx="5" cy="5" r="4" fill="none" stroke="#e0622b"/><path d="M4 3 L6 5 L4 7" fill="none" stroke="#e0622b"/></svg></a>
</section>

<section class="services">
  <span class="abs mark-dot" style="top:1112px;left:203px"></span>
  <div class="abs services-photo" role="img" aria-label="Gloved hands planting yellow primroses and daffodils in soil"></div>
  <h2 class="abs services-band">Our Awesome Services</h2>
  <div class="abs services-tab"></div>
  <p class="abs">Lorem ipsum dolor sit amet, consectetur adipisicing elit, sed do eiusmod tempor incididunt ut labore et dolore magna aliqua. Ut enim ad minim veniam, quis nostrud exercitation ullamco laboris nisi ut aliquip ex ea commodo consequat. Duis aute irure dolor in reprehenderit in voluptate sunt in culpa qui officia deserunt mollit anim id est laborum.</p>
  <a class="abs more-link" style="left:73px;top:1492px" href="#">Order Now
    <svg width="10" height="10" viewBox="0 0 10 10"><circle cx="5" cy="5" r="4" fill="none" stroke="#e0622b"/><path d="M4 3 L6 5 L4 7" fill="none" stroke="#e0622b"/></svg></a>
</section>

<section class="projects">
  <span class="abs mark-dot" style="top:1630px"></span>
  <h2 class="abs heading title">Our Recent Projects</h2>
  <div class="abs tile" style="left:73px;top:1750px;width:334px;height:239px;background:linear-gradient(135deg,#4e7a2c,#8bb34a 50%,#3d5a24)" role="img" aria-label="Vegetable beds with a child gardening"></div>
  <div class="abs tile" style="left:434px;top:1750px;width:332px;height:507px;background:linear-gradient(160deg,#7a6a55,#4a3a2c 40%,#6fa63a 70%,#2f2a24)" role="img" aria-label="Hands transplanting seedlings from a tray"></div>
  <div class="abs tile" style="left:793px;top:1750px;width:332px;height:239px;background:linear-gradient(135deg,#5e8f2f,#9cbf5a 50%,#7a6a4a)" role="img" aria-label="Wooden raised garden beds on a lawn"></div>
  <div class="abs tile" style="left:73px;top:2016px;width:334px;height:241px;background:linear-gradient(135deg,#a0b27a,#5c7d3a 50%,#6f6a5a)" role="img" aria-label="Garden plot beside a greenhouse"></div>
  <div class="abs tile" style="left:793px;top:2016px;width:332px;height:241px;background:linear-gradient(135deg,#8c7a60,#6a8c3a 50%,#5a4a3a)" role="img" aria-label="Rows of raised vegetable beds"></div>
  <a class="abs more-link" style="left:546px;top:2310px" href="#">Explore More
    <svg width="10" height="10" viewBox="0 0 10 10"><circle cx="5" cy="5" r="4" fill="none" stroke="#e0622b"/><path d="M4 3 L6 5 L4 7" fill="none" stroke="#e0622b"/></svg></a>
</section>

<span class="abs mark-dot" style="top:2416px"></span>
<section class="abs testimonial">
  <div class="quote-mark">“</div>
  <blockquote>“Duis aute irure dolor in reprehenderit in voluptate sunt in culpa qui officia deserunt mollit anim id est laborum.”</blockquote>
  <span class="rule"></span>
  <p class="who">Warren Dale</p>
  <p class="role">customer from loremipsum</p>
  <div class="slider-nav">
    <span><svg width="8" height="10" viewBox="0 0 8 10"><path d="M6 1 L2 5 L6 9" fill="none" stroke="#fff" stroke-width="1.8"/></svg></span>
    <span><svg width="8" height="10" viewBox="0 0 8 10"><path d="M2 1 L6 5 L2 9" fill="none" stroke="#fff" stroke-width="1.8"/></svg></span>
  </div>
</section>

<section class="abs cta" role="img" aria-label="Close-up of freshly harvested vegetables on soil">
  <div class="cta-shade"></div>
  <h2>If You Have an Garden Installation Today!</h2>
  <a class="btn" href="#">Order Online Now</a>
</section>

<footer class="abs site-footer">
  <div class="footer-brand"><span class="dot"></span>Fernbrook Plots</div>
  <div class="footer-col" style="left:343px">
    <h4>Quick Links</h4>
    <ul><li>Home</li><li>About us</li><li>Services</li><li>Projects</li><li>Shop</li><li>contact us</li></ul>
  </div>
  <div class="footer-col" style="left:523px">
    <h4>Customer Support</h4>
    <ul><li>My Account</li><li>Order History</li><li>Wish List</li><li>Newsletter</li><li>Help</li></ul>
  </div>
  <div class="footer-col" style="left:723px">
    <h4>Payment Method</h4>
    <div class="cards"><span></span><span></span><span></span><span></span><span></span></div>
  </div>
  <div class="footer-col" style="left:943px">
    <h4>We’re Social Media</h4>
    <div class="socials"><span></span><span></span><span></span><span></span></div>
  </div>
  <p class="copyright">Copyright © 2017 Fernbrook Plots, All Rights Reserved</p>
</footer>

</body>
</html>
```